Business card design needed

I need a business card for my private practice. I would like to see the designs that use bright blue and white. I would like to see similar designs as to the card below:
http://blog.printvarno.com/2009/designing-a-business-card-with-pv-ks517-template.html
I would like to see the back of the card have room for appointment times. Thank you.

Industry/Entity Type
Business
Contact Information for Business Card
Brightwater Counselling & Wellness Services
Helen Dorsey B.Psychology
Registered Psychologist
Building C, Level 3, 14 Marrow Crescent, Canberra, ACT 2601
T: (02) 6287 5912
F: (02) 6287 5930
info@brightwatercounselling.com.au
www.brightwatercounselling.com.au

```html
<!DOCTYPE html>
<html lang="en">
<head>
<meta charset="utf-8">
<title>Brightwater Counselling &amp; Wellness Services — Business Card</title>
<link href="https://fonts.googleapis.com/css2?family=Noto+Serif:wght@400;700&display=swap" rel="stylesheet">
<style>
  :root {
    --backdrop: #e6ebf0;
    --blue: #0a84e0;
    --blue-deep: #0668b8;
    --blue-soft: #3fa2ec;
    --white: #ffffff;
    --white-soft: rgba(255,255,255,0.88);
    --navy: #123a63;
    --line: #b9d6ef;
  }
  * { margin: 0; padding: 0; box-sizing: border-box; }
  html, body {
    width: 1200px; height: 871px; overflow: hidden;
    background: var(--backdrop);
  }
  .canvas { position: relative; width: 1200px; height: 871px; }
  .card {
    position: absolute; left: 240px;
    width: 720px; height: 400px; overflow: hidden;
    font-family: "Noto Serif", Georgia, serif;
    box-shadow: 0 6px 18px rgba(10,40,80,0.18);
  }
  .card--front {
    top: 24px;
    background: linear-gradient(135deg, var(--blue), var(--blue-deep));
  }
  .card--back { top: 447px; background: var(--white); }
  .card__disc { position: absolute; left: 0; top: 0; }

  .practice {
    position: absolute; left: 62px; top: 150px;
    color: var(--white); font-size: 15px; letter-spacing: 0.3px; white-space: nowrap;
  }
  .practice__divider {
    position: absolute; left: 260px; top: 146px;
    width: 2px; height: 56px; background: var(--white);
  }
  .practice__sub {
    position: absolute; left: 272px; top: 182px;
    color: var(--white); font-size: 15px; letter-spacing: 0.3px; white-space: nowrap;
  }
  .person { position: absolute; left: 430px; top: 72px; color: var(--white); }
  .person__name { font-size: 23px; font-weight: 400; letter-spacing: 0.3px; }
  .person__title { font-size: 14px; margin-top: 2px; letter-spacing: 0.3px; }
  .person__rule {
    position: absolute; left: 430px; top: 132px;
    width: 290px; height: 1px; background: var(--white-soft);
  }
  .contact {
    position: absolute; left: 430px; top: 206px;
    color: var(--white-soft); font-size: 13px; line-height: 1.6;
    list-style: none; white-space: nowrap;
  }
  .contact__label { display: inline-block; width: 22px; }
  .contact__web { margin-top: 4px; color: var(--white); }

  .appointment {
    position: absolute; left: 250px; top: 48px; width: 420px;
    color: var(--navy);
  }
  .appointment__title {
    font-size: 20px; font-weight: 400; color: var(--blue-deep);
    padding-bottom: 10px; border-bottom: 1px solid var(--blue);
  }
  .appointment__head, .appointment__row {
    display: grid; grid-template-columns: 1fr 1fr 1fr; column-gap: 18px;
  }
  .appointment__head {
    font-size: 12px; letter-spacing: 1px; text-transform: uppercase;
    color: var(--blue-deep); margin-top: 14px;
  }
  .appointment__row span { height: 34px; border-bottom: 1px solid var(--line); }
  .appointment__note {
    margin-top: 18px; font-size: 12px; color: var(--navy);
  }
  .back__practice {
    position: absolute; left: 40px; top: 176px; width: 150px;
    color: var(--white); font-size: 15px; line-height: 1.5; text-align: center;
  }
</style>
</head>
<body>
<div class="canvas">
  <div class="card card--front">
    <svg class="card__disc" width="720" height="400" viewBox="0 0 720 400" aria-hidden="true">
      <circle cx="180" cy="180" r="225" fill="var(--blue-soft)" opacity="0.75"/>
    </svg>

    <p class="practice">Brightwater Counselling</p>
    <span class="practice__divider"></span>
    <p class="practice__sub">Wellness Services</p>

    <div class="person">
      <h1 class="person__name">Helen Dorsey B.</h1>
      <p class="person__title">Psychology Registered</p>
    </div>
    <span class="person__rule"></span>

    <ul class="contact">
      <li><span class="contact__label">A:</span>Building C, Level 3,</li>
      <li>14 Marrow Crescent, Canberra, ACT 2601</li>
      <li><span class="contact__label">T:</span>(02) 6287 5912</li>
      <li><span class="contact__label">F:</span>(02) 6287 5930</li>
      <li>info@brightwatercounselling.com.au</li>
      <li class="contact__web">www.brightwatercounselling.com.au</li>
    </ul>
  </div>

  <div class="card card--back">
    <svg class="card__disc" width="720" height="400" viewBox="0 0 720 400" aria-hidden="true">
      <circle cx="80" cy="200" r="170" fill="var(--blue)"/>
    </svg>
    <p class="back__practice">Brightwater<br>Counselling &amp;<br>Wellness Services</p>

    <div class="appointment">
      <h2 class="appointment__title">Your Next Appointment</h2>
      <div class="appointment__head"><span>Day</span><span>Date</span><span>Time</span></div>
      <div class="appointment__row"><span></span><span></span><span></span></div>
      <div class="appointment__row"><span></span><span></span><span></span></div>
      <div class="appointment__row"><span></span><span></span><span></span></div>
      <div class="appointment__row"><span></span><span></span><span></span></div>
      <p class="appointment__note">To change an appointment please call (02) 6287 5912</p>
    </div>
  </div>
</div>
</body>
</html>
```